Business card Zottelgarten

Business card is for a self-employed dog trainer with own dog school. Name and logo of the dog school are available. Color specifications as well. The design should be classy and minimalist, but also modern. An already existing idea would be: Front: Only the logo Back: Contact data

Font styles to use
Serif
Sans Serif
Other font styles liked:
• Trajan Pro

Colors
f78f20

Requirements
Must have
• Name: Margit Wendler-Rasch Title: Dipl. Dog Trainer Contain my logo Follow my font and color preferences (see files)

```html
<!DOCTYPE html>
<html lang="en">
<head>
<meta charset="utf-8">
<title>Zottelgarten – Business Card</title>
<link rel="stylesheet" href="https://fonts.googleapis.com/css2?family=Cinzel:wght@400;600&family=Open+Sans:wght@400;600;700&display=swap">
<style>
  :root {
    --backdrop: #3a3330;
    --card: #111010;
    --card-edge: #1d1b1a;
    --tan: #a38d74;
    --tan-dark: #8a765f;
    --ink: #f2f2f2;
    --muted: #bdbdbd;
    --silver: #c9c9c9;
    --silver-dark: #8d8d8d;
    --divider: #3a3634;
  }
  * { box-sizing: border-box; margin: 0; padding: 0; }
  html, body {
    width: 1200px; height: 900px; overflow: hidden;
    background: var(--backdrop);
  }
  .stage {
    position: relative; width: 1200px; height: 900px;
  }
  .card {
    position: absolute; top: 305px;
    width: 510px; height: 290px;
    background: var(--card);
    border: 1px solid var(--card-edge);
    box-shadow: 0 10px 24px rgba(0,0,0,.45);
  }
  /* contact side */
  .card--contact { left: 60px; }
  .card--contact .emblem {
    position: absolute; left: 40px; top: 55px;
    width: 180px; height: 180px; border-radius: 50%;
    background: var(--tan);
    box-shadow: 0 0 0 3px var(--card), 0 0 0 4px var(--tan-dark);
    display: flex; align-items: center; justify-content: center;
  }
  .emblem__name {
    font-family: 'Open Sans', sans-serif; font-weight: 700;
    font-size: 19px; color: var(--card); letter-spacing: .5px;
  }
  .card--contact .divider {
    position: absolute; left: 262px; top: 58px;
    width: 1px; height: 178px; background: var(--divider);
  }
  .details {
    position: absolute; left: 282px; top: 58px;
    font-family: 'Open Sans', sans-serif; color: var(--ink);
    font-size: 13px; line-height: 1.35;
  }
  .details__name { color: var(--tan); font-weight: 700; font-size: 17px; line-height: 1.2; }
  .details__title { margin-bottom: 14px; }
  .details__address { margin-bottom: 12px; }
  .details__row { display: flex; align-items: center; gap: 9px; }
  .details__row svg { width: 10px; height: 10px; fill: var(--tan); flex: none; }
  /* brand side */
  .card--brand { left: 630px; text-align: center; }
  .card--brand .seal {
    width: 128px; height: 128px; margin: 36px auto 0; border-radius: 50%;
    background: radial-gradient(circle at 40% 35%, #e2e2e2, var(--silver) 55%, var(--silver-dark));
    box-shadow: 0 0 0 3px var(--card), 0 0 0 4px var(--silver-dark);
  }
  .brand__name {
    margin-top: 22px;
    font-family: 'Cinzel', serif; font-weight: 600;
    font-size: 34px; letter-spacing: 3px; color: var(--silver);
  }
  .brand__web {
    margin-top: 2px;
    font-family: 'Cinzel', serif; font-size: 10px;
    letter-spacing: 5px; color: var(--silver-dark);
  }
</style>
</head>
<body>
<main class="stage">
  <section class="card card--contact" aria-label="Business card, contact side">
    <div class="emblem"><span class="emblem__name">Zottelgarten</span></div>
    <div class="divider"></div>
    <div class="details">
      <p class="details__name">Margit Wendler-Rasch</p>
      <p class="details__title">Dipl. Dog Trainer</p>
      <p class="details__address">12345, Address Goes Here<br>Country Name, 123456.</p>
      <p class="details__row">
        <svg viewBox="0 0 10 10"><path d="M2 0.5l1.6 2.2-1 1c.6 1.3 1.5 2.2 2.7 2.8l1-1L8.5 7 7.6 9C4 8.6 1.3 5.8 0.8 2.2z"/></svg>
        044-123 456 789
      </p>
      <p class="details__row">
        <svg viewBox="0 0 10 10"><path d="M0 2h10v6H0zM0.8 2.5L5 5.6 9.2 2.5v-.1L5 4.7.8 2.4z"/></svg>
        info@webname.com
      </p>
      <p class="details__row">
        <svg viewBox="0 0 10 10"><path d="M4 6.8L3 7.8a1.3 1.3 0 01-1.8-1.8l2-2a1.3 1.3 0 011.8 0l.7-.7a2.3 2.3 0 00-3.2 0l-2 2a2.3 2.3 0 003.2 3.2l1-1zM6 3.2l1-1a1.3 1.3 0 011.8 1.8l-2 2a1.3 1.3 0 01-1.8 0l-.7.7a2.3 2.3 0 003.2 0l2-2a2.3 2.3 0 00-3.2-3.2l-1 1z"/></svg>
        www.websitename.com
      </p>
    </div>
  </section>

  <section class="card card--brand" aria-label="Business card, brand side">
    <div class="seal"></div>
    <p class="brand__name">ZOTTELGARTEN</p>
    <p class="brand__web">WWW.ZOTTELGARTEN.CH</p>
  </section>
</main>
</body>
</html>
```